Brochure Design Needed for Water Savings Solutions Company

Our company is called Meridel Field Partners of Norvania (or MFP) and is looking for a stylish brochure for sales opportunites. We engage clients who are mostly professional property owners in commercial real estate settings and offer irrigation saving solutions utilizing cutting edge technologies that can be managed via computer, smart phone and tablets. The technology we use is wireless and uses real time weather information to communicate water schedules based on specific site and plant details. Our core program offers clients a free service (funded by us) with payments only occuring if savings are achieved. We also offer irrigation monitoring services and design consulting, but want to focus on the partnership agreement.

Target Market(s)

30-40 year old property management professionals with college and above education levels, 60% female and typically white

Industry/Entity Type

Real Estate

Requirements
Nice to have
• A bi fold contemporary brochure is preferred. Incorporation of website themes, pictures and colors is a plus and can be located at mfpbrook.example. Since this is a water conservation company, some consideration should be paid to water and green ideas.

```html
<!DOCTYPE html>
<html lang="en">
<head>
<meta charset="utf-8">
<title>MFP Water Brochure</title>
<link href="https://fonts.googleapis.com/css2?family=Open+Sans:wght@300;400;600&display=swap" rel="stylesheet">
<style>
:root{
  --backdrop:#17191b;
  --paper:#ffffff;
  --ink:#3a3a3a;
  --body:#555555;
  --green:#5b9e2d;
  --teal:#3fb0cc;
  --callout:#5ec3d8;
  --band-top:#4a4c4e;
  --band-bottom:#1e2022;
}
*{margin:0;padding:0;box-sizing:border-box}
html,body{width:848px;height:1200px;overflow:hidden;background:var(--backdrop);font-family:"Open Sans",Arial,sans-serif;color:var(--ink)}
.canvas{position:relative;width:848px;height:1200px}
.spread{position:absolute;left:22px;width:804px;background:var(--paper)}
.spread--outer{top:19px;height:570px}
.spread--inner{top:610px;height:572px}
.page{position:absolute;top:0;height:100%}
.page--left{left:0;width:402px}
.page--right{left:402px;width:402px}
.placeholder{position:absolute}
.leaves-deco{left:110px;top:0;width:260px;height:190px;background:radial-gradient(ellipse at 55% 40%,#e6f2cf 0%,#f4f9ec 45%,rgba(255,255,255,0) 75%)}
.hero-photo{left:0;top:0;width:402px;height:570px;background:linear-gradient(160deg,#ffffff 0%,#f3f6ee 30%,#c9dd9a 45%,#6fa830 55%,#e9c4aa 70%,#d9a98d 85%,#f1ddd0 100%)}
.piggy-art{left:52px;top:95px;width:300px;height:230px;background:radial-gradient(ellipse at 50% 60%,#d8dcdc 0%,#b89b6c 30%,#e9f1dc 55%,rgba(255,255,255,0) 78%)}
.handshake-photo{left:0;top:267px;width:402px;height:240px;background:linear-gradient(120deg,#cfe6f5 0%,#9fcbe6 35%,#f1d6c4 55%,#5f86b8 75%,#2f4f86 100%)}
.heading{position:absolute;font-weight:300;font-size:16px;letter-spacing:.5px;color:var(--ink);text-transform:uppercase}
.body-copy{position:absolute;font-size:6.3px;line-height:8.4px;color:var(--body);text-align:justify}
.url{position:absolute;font-size:10px;letter-spacing:6px;color:var(--green)}
.tagline{position:absolute;left:28px;top:56px;width:230px;font-size:14.5px;line-height:15px;font-weight:400;color:var(--green);text-transform:uppercase}
.brand{position:absolute;left:128px;top:467px;display:flex;align-items:center;gap:6px}
.brand-dot{width:22px;height:22px;border-radius:50%;background:var(--green)}
.brand-name{font-size:12px;font-weight:600;color:var(--green);line-height:13px}
.brand-sub{font-size:4.6px;font-weight:600;color:var(--green);line-height:6px}
.callout{position:absolute;background:var(--callout);color:#fff;font-size:7px;line-height:8px;text-align:center;padding:3px 5px;border:2px solid #fff;border-radius:3px;box-shadow:0 0 2px rgba(0,0,0,.25)}
.steps{position:absolute;left:28px;top:94px;width:340px;list-style:none}
.step{position:relative;padding-left:16px;margin-bottom:9px}
.step-drop{position:absolute;left:0;top:1px;width:10px;height:12px}
.step-title{font-size:11.5px;font-weight:400;color:var(--teal);text-transform:uppercase;line-height:14px}
.step-text{font-size:6.3px;line-height:8px;color:var(--body)}
.cta{position:absolute;left:30px;top:226px;font-size:15px;color:var(--teal)}
.footer-band{position:absolute;left:0;bottom:0;width:804px;height:64px;background:linear-gradient(var(--band-top),var(--band-bottom))}
.footer-band .url{color:#d8d8d8;top:14px}
</style>
</head>
<body>
<div class="canvas">

  <section class="spread spread--outer">
    <div class="page page--left">
      <div class="placeholder leaves-deco" role="img" aria-label="Faint green leaves with water droplets"></div>
      <h2 class="heading" style="left:32px;top:175px">Why We Exist</h2>
      <p class="body-copy" style="left:32px;top:196px;width:356px">Automated irrigation of landscapes and outdoor spaces is intended to supplement the lack of rainfall in periods of extreme heat and dry conditions throughout the year. Most areas of the US would not be able to sustain green turf grasses and colorful flowers without the use of irrigation throughout the summer months, which could lead to diminished curb appeal for businesses and the loss of expensive plants. The irrigation system becomes an insurance policy for green spaces and property owners alike. At the same time, the mismanagement of irrigation systems can lead to many problems for these same plants and property owners. Overuse and waste of irrigation water leaches fertilizers out of the plant's root system, invites insects and diseases into the landscape, blocks oxygen from the soil AND costs businesses a lot of money! There is only a certain amount of water each specific plant, tree, grass or flower needs and can absorb on a daily basis. Any water applied after that threshold is reached is considered waste. With new technologies based on specific plant water requirements and daily weather based information, MFP helps customers understand and manage water use for each site. MFP tracks monthly water usage through wireless communication with controllers, emails system problems to property managers and analyzes weather patterns to determine if watering schedules are accurate. MFP's interest is to help customers protect their landscapes and associated expenses as well as preserve the environment.</p>
      <span class="url" style="left:88px;top:518px">mfpbrook.example</span>
    </div>
    <div class="page page--right">
      <div class="placeholder hero-photo" role="img" aria-label="Cupped hands holding soil with a green seedling covered in water drops"></div>
      <h1 class="tagline">Conserve water, save money and make a positive impact on the environment</h1>
      <div class="brand">
        <span class="brand-dot"></span>
        <div>
          <div class="brand-name">MFPBROOK.EXAMPLE</div>
          <div class="brand-sub">MERIDEL FIELD PARTNERS OF NORVANIA</div>
        </div>
      </div>
    </div>
  </section>

  <section class="spread spread--inner">
    <div class="page page--left">
      <h2 class="heading" style="left:32px;top:20px">Water Monitoring Solutions</h2>
      <p class="body-copy" style="left:32px;top:44px;width:348px">Achieving landscape water efficiency requires analyzing past water usage and developing water budgets for new landscapes. MFP has the knowledge and experience to develop programs that conserve water through science, technology and real time communication. Whether it's installing and managing weather based smart controllers or sending leak and rainfall alerts via email, MFP ensures that our clients benefit from the latest technologies and fastest communication methods available.</p>
      <div class="placeholder piggy-art" role="img" aria-label="Glass piggy bank filled with coins with a green sprout growing from it"></div>
      <div class="callout" style="left:172px;top:119px;width:92px">No capital requirements for components</div>
      <div class="callout" style="left:52px;top:215px;width:92px">No payments unless savings are realized</div>
      <div class="callout" style="left:250px;top:200px;width:92px">Flexible contract terms</div>
      <div class="callout" style="left:54px;top:360px;width:88px">Onsite technology and equipment managed by MFP</div>
      <div class="callout" style="left:250px;top:360px;width:92px">Instant Green technology marketing opportunities</div>
      <p class="body-copy" style="left:32px;top:416px;width:348px">MFP offers water saving programs to clients with maximum benefits and low risks. Our philosophy on water conservation is backed by our commitment to carry the upfront costs necessary to install new equipment. MFP takes a hands on management approach with clients during the contract term and only receives payment if the client reduces water usage.</p>
    </div>
    <div class="page page--right">
      <h2 class="heading" style="left:30px;top:20px">Getting Started Is Simple</h2>
      <p class="body-copy" style="left:30px;top:44px;width:346px">The MFP water management approach works the same regardless of property size or location. Our programs are scalable to all properties that utilize automated irrigation. The technologies we implement provide efficient irrigation control systems for properties that can be managed by smartphone, tablet or computer. Let MFP create a truly mobile experience that can easily manage as many properties as needed through one convenient service.</p>
      <ul class="steps">
        <li class="step">
          <svg class="step-drop" viewBox="0 0 10 12"><path d="M5 0C3 4 0 6 0 8.2A5 5 0 0 0 10 8.2C10 6 7 4 5 0Z" fill="#3fb0cc"/></svg>
          <div class="step-title">Establish a Water Budget</div>
          <div class="step-text">Analyze historical water bills, develop a budget and evaluate savings opportunities based on current water usage.</div>
        </li>
        <li class="step">
          <svg class="step-drop" viewBox="0 0 10 12"><path d="M5 0C3 4 0 6 0 8.2A5 5 0 0 0 10 8.2C10 6 7 4 5 0Z" fill="#3fb0cc"/></svg>
          <div class="step-title">Conduct a Site Audit</div>
          <div class="step-text">Assess landscape, irrigation scheduling, plant types per zones and validate water budget.</div>
        </li>
        <li class="step">
          <svg class="step-drop" viewBox="0 0 10 12"><path d="M5 0C3 4 0 6 0 8.2A5 5 0 0 0 10 8.2C10 6 7 4 5 0Z" fill="#3fb0cc"/></svg>
          <div class="step-title">Implement a Custom Program</div>
          <div class="step-text">Design a partnership agreement unique to your property, install water saving devices, monitor plant and irrigation components and generate monthly usage reports.</div>
        </li>
      </ul>
      <p class="cta">Contact Us To Get Started!</p>
      <div class="placeholder handshake-photo" role="img" aria-label="Business handshake between two professionals in an office"></div>
    </div>
    <div class="footer-band">
      <span class="url" style="left:88px">mfpbrook.example</span>
      <span class="url" style="left:490px">mfpbrook.example</span>
    </div>
  </section>

</div>
</body>
</html>
```